Business Card Design Project

We require a professional business card designed for our consulting organisation that has the same theme and colours as our logo except for the grey.

Colours on the front should predominately be white however some reference to our logo colours except for the grey.

The back of the card should be have background colour that aligns with our logo colour.

Layout, style and design is up to the designer. So send through your designs

Details are attached in the word document project brief.

Target Market(s)

Target market are large corporate organisations

Industry/Entity Type

Business

Requirements
Must have
• Content on the front must have:

Dale Fenwick
Managing Director

P: 0412 557 208
E: Dale@braviotraxgroup.com
W: www.braviotraxgroup.com

Content on the back must have the words:
Alliances
Placement
Training
Support

Design Colours
Must align to our logo

```html
<!DOCTYPE html>
<html lang="en">
<head>
<meta charset="utf-8">
<title>Braviotrax Group – Business Card</title>
<link href="https://fonts.googleapis.com/css2?family=Arimo:wght@400;700&display=swap" rel="stylesheet">
<style>
  :root {
    --page-bg: #ffffff;
    --card-white: #f4f4f4;
    --card-edge: #e6e6e6;
    --brand-blue: #1f7fc4;
    --band-blue: #4a9fd6;
    --back-blue-deep: #2f7fc0;
    --back-blue-light: #5ab4e4;
    --text-name: #7a7a7a;
    --text-title: #9a9a9a;
    --text-contact: #a3a3a3;
    --icon-grey: #4a4a4a;
    --text-on-blue: #ffffff;
  }
  * { margin: 0; padding: 0; box-sizing: border-box; }
  html, body {
    width: 1200px; height: 1000px; overflow: hidden;
    background: var(--page-bg);
    font-family: "Arimo", Arial, sans-serif;
  }
  .card {
    position: absolute; left: 212px; width: 784px; overflow: hidden;
  }
  .card-front {
    top: 35px; height: 453px;
    background: radial-gradient(ellipse at 55% 40%, #ffffff 0%, var(--card-white) 55%, var(--card-edge) 100%);
  }
  .front-band {
    position: absolute; left: 0; bottom: 0; width: 100%; height: 44px;
    background: linear-gradient(90deg, var(--back-blue-deep), var(--band-blue) 50%, var(--back-blue-deep));
  }
  .brand {
    position: absolute; top: 160px; left: 0; width: 100%;
    display: flex; justify-content: center; align-items: center; gap: 18px;
  }
  .brand-dot {
    width: 58px; height: 58px; border-radius: 50%; background: var(--brand-blue);
  }
  .brand-name {
    font-size: 44px; font-weight: 700; color: var(--brand-blue); letter-spacing: 0.5px;
  }
  .person {
    position: absolute; top: 320px; right: 445px; text-align: right;
  }
  .person-name {
    font-size: 24px; color: var(--text-name); letter-spacing: 0.5px; text-transform: uppercase;
  }
  .person-title {
    margin-top: 6px; font-size: 20px; color: var(--text-title); letter-spacing: 1.5px;
  }
  .contact {
    position: absolute; top: 321px; left: 379px; list-style: none;
  }
  .contact li {
    display: flex; align-items: center; height: 23px;
    font-size: 16px; font-weight: 700; color: var(--text-contact); letter-spacing: 1px;
  }
  .contact svg { width: 18px; height: 18px; margin-right: 14px; fill: var(--icon-grey); }
  .card-back {
    top: 514px; height: 452px;
    background: radial-gradient(ellipse at 50% 40%, var(--back-blue-light) 0%, #4aa6da 45%, var(--back-blue-deep) 100%);
  }
  .services {
    position: absolute; top: 224px; left: 0; width: 100%;
    display: flex; justify-content: center; align-items: center; gap: 8px;
    font-size: 26px; color: var(--text-on-blue); letter-spacing: 0.5px; text-transform: uppercase;
  }
  .services .divider {
    width: 5px; height: 24px;
    background: linear-gradient(180deg, #ffffff, #cfcfcf);
  }
</style>
</head>
<body>
  <section class="card card-front">
    <div class="brand">
      <span class="brand-dot"></span>
      <span class="brand-name">Braviotrax Group</span>
    </div>

    <div class="person">
      <p class="person-name">Dale Fenwick</p>
      <p class="person-title">managing director</p>
    </div>

    <ul class="contact">
      <li>
        <svg viewBox="0 0 24 24" aria-hidden="true"><path d="M6.6 10.8a15 15 0 0 0 6.6 6.6l2.2-2.2a1 1 0 0 1 1-.25 11.4 11.4 0 0 0 3.6.6 1 1 0 0 1 1 1V20a1 1 0 0 1-1 1A17 17 0 0 1 3 4a1 1 0 0 1 1-1h3.5a1 1 0 0 1 1 1c0 1.25.2 2.45.6 3.6a1 1 0 0 1-.25 1z"/></svg>
        0412 557 208
      </li>
      <li>
        <svg viewBox="0 0 24 24" aria-hidden="true"><path d="M2 5h20v14H2z M3 6.5v.5l9 6 9-6v-.5z" fill-rule="evenodd"/></svg>
        Dale@braviotraxgroup.com
      </li>
      <li>
        <svg viewBox="0 0 24 24" aria-hidden="true"><circle cx="12" cy="12" r="10"/><path d="M2 12h20M12 2a15 15 0 0 1 0 20M12 2a15 15 0 0 0 0 20" stroke="#f4f4f4" stroke-width="1.4" fill="none"/></svg>
        www.braviotraxgroup.com
      </li>
    </ul>

    <div class="front-band"></div>
  </section>

  <section class="card card-back">
    <div class="services">
      <span>Alliances</span><span class="divider"></span>
      <span>Placement</span><span class="divider"></span>
      <span>Training</span><span class="divider"></span>
      <span>Support</span>
    </div>
  </section>
</body>
</html>
```